Ray Hollin Foundation
Business card and letterhead for a non profit
Professional
Marissa Hollin
P.O. Box 83 Glenmere Ridge, PA 18261
rayhollinfoundation@mailvesta.org
www.rayhollinfoundation.org
Business card: I would like the foundation logo to be the one side. Then information on the other side.

```html
<!DOCTYPE html>
<html lang="en">
<head>
<meta charset="utf-8">
<title>Ray Hollin Foundation – Business Card</title>
<link rel="stylesheet" href="https://fonts.googleapis.com/css2?family=Libre+Baskerville:wght@400;700&display=swap">
<style>
  :root {
    --backdrop: #d9d9d9;
    --card-black: #0b0b0b;
    --card-blue: #2b8fd6;
    --blue-deep: #1f76b8;
    --brand-green: #22b24c;
    --banner-green: #2fb34a;
    --ink-dark: #12263a;
    --white: #ffffff;
  }
  * { margin: 0; padding: 0; box-sizing: border-box; }
  html, body { width: 1200px; height: 799px; overflow: hidden; }
  body {
    background: var(--backdrop);
    font-family: "Libre Baskerville", Georgia, serif;
    position: relative;
  }
  .card {
    position: absolute;
    width: 520px;
    height: 300px;
    border-radius: 16px;
    overflow: hidden;
  }

  /* Front: foundation name */
  .card-front {
    left: 80px;
    top: 410px;
    background: var(--card-black);
    display: flex;
    align-items: center;
    justify-content: center;
    gap: 18px;
  }
  .brand-dot {
    width: 34px; height: 34px;
    border-radius: 50%;
    background: var(--brand-green);
    flex: none;
  }
  .brand-name {
    color: var(--brand-green);
    font-weight: 700;
    font-size: 30px;
    letter-spacing: 1px;
  }

  /* Back: contact details */
  .card-back {
    left: 600px;
    top: 90px;
    background: var(--card-blue);
  }
  .name-banner {
    position: absolute;
    left: 0; top: 24px;
    width: 330px; height: 50px;
    background: var(--banner-green);
    clip-path: polygon(0 0, 100% 0, 100% 100%, 0 100%);
    display: flex; align-items: center;
    padding-left: 60px;
  }
  .name-banner::after {
    content: "";
    position: absolute;
    right: -1px; top: 0;
    width: 0; height: 0;
  }
  .holder-name {
    color: var(--white);
    font-size: 22px;
    font-variant: small-caps;
    letter-spacing: 1px;
  }
  .address-band {
    position: absolute;
    right: 0; top: 150px;
    width: 190px; height: 52px;
    background: var(--banner-green);
    clip-path: polygon(14% 0, 100% 0, 100% 100%, 0 100%);
    color: var(--white);
    font-size: 10px;
    font-variant: small-caps;
    line-height: 1.5;
    padding: 10px 0 0 40px;
  }
  .contact-list {
    position: absolute;
    left: 24px; top: 96px;
    list-style: none;
  }
  .contact-item {
    display: flex; align-items: center;
    gap: 16px;
    height: 27px;
    color: var(--ink-dark);
    font-size: 13px;
  }
  .contact-icon {
    width: 18px; height: 18px;
    flex: none;
  }
  .faint-mark {
    position: absolute;
    right: 90px; bottom: 26px;
    width: 80px; height: 80px;
    border-radius: 50%;
    background: var(--blue-deep);
    opacity: 0.5;
  }
</style>
</head>
<body>

  <section class="card card-back" aria-label="Business card back">
    <div class="name-banner"><span class="holder-name">Marissa Hollin</span></div>

    <ul class="contact-list">
      <li class="contact-item">
        <svg class="contact-icon" viewBox="0 0 18 18"><circle cx="9" cy="9" r="9" fill="#fff"/><path d="M6 5 l2 0 l1 2.5 l-1.2 1 a6 6 0 0 0 2.7 2.7 l1 -1.2 l2.5 1 l0 2 a1 1 0 0 1 -1 1 a8 8 0 0 1 -8 -8 a1 1 0 0 1 1 -1z" fill="#2b8fd6"/></svg>
        <span>555-310-2846</span>
      </li>
      <li class="contact-item">
        <svg class="contact-icon" viewBox="0 0 18 18"><circle cx="9" cy="9" r="9" fill="#fff"/><rect x="6" y="4" width="6" height="10" rx="1" fill="#2b8fd6"/><rect x="7" y="5.5" width="4" height="6" fill="#fff"/></svg>
        <span>555-718-9032</span>
      </li>
      <li class="contact-item">
        <svg class="contact-icon" viewBox="0 0 18 18"><circle cx="9" cy="9" r="9" fill="#fff"/><rect x="4" y="5.5" width="10" height="7" fill="#2b8fd6"/><path d="M4 5.5 l5 4 l5 -4" stroke="#fff" stroke-width="1" fill="none"/></svg>
        <span>rayhollinfoundation@mailvesta.org</span>
      </li>
      <li class="contact-item">
        <svg class="contact-icon" viewBox="0 0 18 18"><circle cx="9" cy="9" r="9" fill="#fff"/><circle cx="9" cy="9" r="5" fill="none" stroke="#2b8fd6" stroke-width="1.2"/><path d="M4 9 h10 M9 4 c-3 3 -3 7 0 10 M9 4 c3 3 3 7 0 10" stroke="#2b8fd6" stroke-width="1" fill="none"/></svg>
        <span>www.rayhollinfoundation.org</span>
      </li>
    </ul>

    <div class="address-band">P.O. Box 83<br>Glenmere Ridge, PA 18261</div>
    <div class="faint-mark" role="img" aria-label="Faint foundation emblem area"></div>
  </section>

  <section class="card card-front" aria-label="Business card front">
    <span class="brand-dot"></span>
    <span class="brand-name">Ray Hollin Foundation</span>
  </section>

</body>
</html>
```